Wine Bottle Label for Rosa Hartwell California Wine

This will be a wine bottle label. The wine is produced from grapes from our family farm. Images at bottom are some of same ones in high resolution

Rosa Hartwell
Reserve Pinot Noir
Clarksburg 2023
Estate Grown (in cursive)

We would like to have a view from above, looking down from the levee there is a slough (wing of a river) running behind it, it looks down over vineyards, a big wood barn, a giant Oak Tree beyond the barn. There are beautiful sunsets there in the distance. Many birds fly over the vineyards including small black birds (as shown in one photo). Please use what you can from these suggestions to make a label. We will need a small image for back label and wording on it.

Other font styles liked:
• Wine bottle fonts

Requirements
Must have
• Wording mentioned . An Oak Tree with images of the vines and a sunset
Nice to have
• Flock of black birds flying in the sky

```html
<!DOCTYPE html>
<html lang="en">
<head>
<meta charset="utf-8">
<title>Rosa Hartwell Reserve Pinot Noir Label</title>
<link href="https://fonts.googleapis.com/css2?family=Great+Vibes&family=Dancing+Script:wght@700&family=Cormorant+Garamond:wght@500;600&display=swap" rel="stylesheet">
<style>
  :root {
    --backdrop: #d9d1bd;
    --paper: #fbfbf9;
    --gold: #c9a033;
    --gold-deep: #b08620;
    --ink: #1d1d1d;
    --rule: #3a3a3a;
    --grey-light: #e4e4e2;
    --grey-mid: #9a9a98;
    --grey-dark: #4a4a4a;
  }
  * { margin: 0; padding: 0; box-sizing: border-box; }
  html, body {
    width: 1200px;
    height: 800px;
    overflow: hidden;
    background: var(--backdrop);
  }
  .canvas {
    position: relative;
    width: 1200px;
    height: 800px;
    display: flex;
    align-items: center;
    justify-content: center;
  }
  .label {
    position: relative;
    width: 940px;
    height: 720px;
    background: var(--paper);
    box-shadow: 0 4px 18px rgba(0,0,0,0.12);
    display: flex;
    flex-direction: column;
    align-items: center;
  }
  .top-rule {
    position: absolute;
    top: 34px;
    left: 0;
    right: 0;
    height: 2px;
    background: var(--rule);
  }
  .seal {
    margin-top: 62px;
    width: 46px;
    height: 46px;
    border-radius: 50%;
    background: var(--gold);
    border: 2px solid var(--gold-deep);
  }
  .brand-name {
    margin-top: 6px;
    font-family: "Great Vibes", cursive;
    font-size: 92px;
    line-height: 1.05;
    color: var(--gold);
    font-weight: 400;
  }
  .varietal {
    margin-top: 2px;
    font-family: "Cormorant Garamond", serif;
    font-weight: 500;
    font-size: 28px;
    letter-spacing: 0.32em;
    color: var(--ink);
    text-transform: uppercase;
  }
  .estate {
    margin-top: 0;
    font-family: "Dancing Script", cursive;
    font-weight: 700;
    font-size: 40px;
    color: var(--ink);
  }
  .scene {
    margin-top: 18px;
    width: 360px;
    height: 250px;
    border-radius: 18px 40px 22px 50px;
    background:
      radial-gradient(ellipse at 30% 25%, var(--grey-light) 0%, transparent 55%),
      linear-gradient(160deg, var(--grey-light) 0%, var(--grey-mid) 55%, var(--grey-dark) 100%);
  }
  .appellation {
    margin-top: 26px;
    font-family: "Cormorant Garamond", serif;
    font-weight: 600;
    font-size: 24px;
    letter-spacing: 0.14em;
    font-variant: small-caps;
    color: var(--ink);
  }
  .base-bands {
    position: absolute;
    left: 0;
    right: 0;
    bottom: 22px;
  }
  .base-bands .band-thick {
    height: 5px;
    background: var(--gold);
  }
  .base-bands .band-thin {
    margin-top: 4px;
    height: 2px;
    background: var(--gold-deep);
  }
</style>
</head>
<body>
  <div class="canvas">
    <section class="label">
      <div class="top-rule"></div>
      <div class="seal" aria-hidden="true"></div>
      <h1 class="brand-name">Rosa Hartwell</h1>
      <p class="varietal">Reserve Pinot Noir</p>
      <p class="estate">Estate Grown</p>
      <div class="scene" role="img" aria-label="Grayscale painted view of the estate: vineyard rows, a large wooden barn and an oak tree"></div>
      <p class="appellation">Clarksburg 2023</p>
      <div class="base-bands">
        <div class="band-thick"></div>
        <div class="band-thin"></div>
      </div>
    </section>
  </div>
</body>
</html>
```